Flyer for spiritual retreat (yoga, meditation, reiki, raw food)

I would like a flyer to promote my upcoming retreat and a matching Facebook banner.

The name of the retreat is "Wavecrest Of Calm" and the tagline is "retreat into you"

The activities in the retreat include daily meditation, ecstatic dance, spiritual development workshops on intuition, energy healing etc and a reiki session is included.

I would like a flyer designed to promote this, something that is editable as I will be running this multiple times and will need to adjust the flyer to add the dates etc each time.

edit: add that here will be fully catered raw food and juices, and that the retreat price includes all accomodation, meals and workshops.

Please contact me if you need further info. Please also visit my website www.marithovland.com and www.facebook.com/tolvanahaven to see my current events and promotions.

Thank you,

Marit

Reason: Hi all, thank you all for your submissions. Apologies as I am traveling and do not have much access to internet and will review your submissions and provide feedback as soon as possible. Kind regards, Marit.

Target Market(s)

People who like meditation, yoga, fans of rowan mabry and jasper vinek, those interested in personal and spiritual development.

Industry/Entity Type

Health And Wellness

Requirements
Must have
• Please put the included reiki session as as added bonus. Something like "BONUS 30 minute reiki healing session" in a little star/banner/something that stands out.
• Please emphasise the "light" part of Wavecrest as I am going for a play on words between in the light and enlightenment.
• Please include placeholder text for place, location, time
• Placeholder for price
• My name (see attached file - can change colour to suit) and website (www.marithovland.com)
Nice to have
• I prefer rounded designs, curves rather than block designs.
Should not have
• Tolvana Haven logo

```html
<!DOCTYPE html>
<html lang="en">
<head>
<meta charset="utf-8">
<title>Wavecrest Of Calm – retreat into you</title>
<link rel="stylesheet" href="https://fonts.googleapis.com/css2?family=Marcellus&family=Great+Vibes&family=Allura&family=Montserrat:wght@300&family=Playfair+Display:ital,wght@1,400&family=Libre+Baskerville:wght@400;700&family=Oswald:wght@500&display=swap">
<style>
  :root {
    --night: #221f20;
    --nebula-gold: #9c7d2c;
    --nebula-amber: #6b4d1d;
    --glow: #fff3c2;
    --gold: #d8b25a;
    --gold-deep: #a8782c;
    --cream: #f5ecb0;
    --white: #ffffff;
    --bonus-yellow: #f4e70b;
    --ink: #1e1b1c;
    --dot: #e6d477;
    --price-bg: #faf3b9;
  }
  * { margin: 0; padding: 0; box-sizing: border-box; }
  html, body { width: 848px; height: 1200px; overflow: hidden; background: var(--night); }
  .flyer {
    position: relative; width: 848px; height: 1200px; overflow: hidden;
    background:
      radial-gradient(ellipse 520px 300px at 380px 330px, rgba(196,160,64,.55), transparent 70%),
      radial-gradient(ellipse 300px 220px at 140px 200px, rgba(150,110,40,.45), transparent 70%),
      radial-gradient(ellipse 360px 200px at 620px 460px, rgba(120,100,40,.4), transparent 70%),
      linear-gradient(180deg, #2a2622 0%, #3a3024 30%, #2c2722 55%, var(--night) 68%);
  }
  .hero-art {
    position: absolute; left: 188px; top: 60px; width: 436px; height: 492px;
    background: radial-gradient(ellipse 120px 180px at 50% 45%, var(--glow), rgba(216,178,90,.6) 45%, rgba(168,120,44,.15) 80%, transparent 100%);
  }
  .title {
    position: absolute; left: 64px; top: 520px; width: 740px;
    display: flex; align-items: baseline; white-space: nowrap;
    font-family: "Marcellus", serif; font-size: 68px; color: var(--white);
  }
  .title .script {
    font-family: "Great Vibes", cursive; font-size: 132px; line-height: 1;
    color: var(--gold); margin: 0 10px 0 2px;
    text-shadow: 0 0 14px rgba(255,230,160,.35);
  }
  .tagline {
    position: absolute; left: 268px; top: 620px;
    font-family: "Montserrat", sans-serif; font-weight: 300; font-size: 32px;
    letter-spacing: 14px; color: var(--white);
  }
  .activities {
    position: absolute; left: 54px; top: 706px; width: 560px;
    font-family: "Playfair Display", serif; font-style: italic; font-size: 23px;
    line-height: 40px; color: var(--cream);
  }
  .bonus {
    position: absolute; left: 632px; top: 678px; width: 168px; height: 168px;
    border: 2px solid var(--cream); border-radius: 50%;
    display: flex; flex-direction: column; align-items: center; justify-content: center;
    text-align: center; color: var(--white);
    font-family: "Libre Baskerville", serif; font-size: 18px; line-height: 22px;
    box-shadow: 0 0 18px rgba(255,240,180,.2);
  }
  .bonus-label {
    font-family: "Oswald", sans-serif; font-weight: 500; font-size: 28px;
    line-height: 34px; color: var(--bonus-yellow); margin-bottom: 4px;
  }
  .details {
    position: absolute; left: 94px; top: 870px; width: 661px; height: 196px;
    background: var(--white); border-radius: 9px; overflow: hidden;
    font-family: "Libre Baskerville", serif; font-weight: 700; font-size: 15px; color: var(--ink);
  }
  .field { position: absolute; left: 20px; display: flex; align-items: baseline; gap: 12px; }
  .field .fill { flex: 1; border-bottom: 2px dotted var(--dot); height: 1px; }
  .field.wide { width: 610px; }
  .field.short { width: 427px; }
  .price {
    position: absolute; left: 448px; top: 123px; width: 213px; height: 73px;
    background: var(--price-bg); padding: 10px 0 0 10px;
  }
  .price .currency { display: block; margin: 4px 0 0 52px; font-size: 20px; }
  .host-photo {
    position: absolute; left: 70px; top: 1090px; width: 80px; height: 80px; border-radius: 50%;
    border: 3px solid var(--white);
    background: radial-gradient(circle at 50% 40%, #b59483, #4a3a33 70%, #6d8466);
  }
  .host-name {
    position: absolute; left: 168px; top: 1100px;
    font-family: "Allura", cursive; font-size: 40px; color: var(--white);
    text-shadow: 0 0 8px rgba(255,255,255,.6);
  }
  .website {
    position: absolute; right: 40px; top: 1138px;
    font-family: "Playfair Display", serif; font-style: italic; font-size: 22px; color: var(--white);
  }
</style>
</head>
<body>
<main class="flyer">
  <div class="hero-art" role="img" aria-label="Golden glowing figure standing inside a star tetrahedron wireframe against a cosmic nebula"></div>

  <h1 class="title">Wave<span class="script">crest</span>Of Calm</h1>
  <p class="tagline">retreat into you</p>

  <p class="activities">The activities in the retreat include daily meditation, ecstatic dance, spiritual development workshops on intuition, energy healing etc</p>

  <div class="bonus">
    <span class="bonus-label">BONUS</span>
    <span>30 minute<br>Reiki Healing<br>Session</span>
  </div>

  <section class="details">
    <div class="field wide" style="top:34px">PLACE<span class="fill"></span></div>
    <div class="field wide" style="top:76px">LOCATION<span class="fill"></span></div>
    <div class="field short" style="top:118px">DATE<span class="fill"></span></div>
    <div class="field short" style="top:160px">TIME<span class="fill"></span></div>
    <div class="price">PRICE<span class="currency">A$</span></div>
  </section>

  <div class="host-photo" role="img" aria-label="Portrait photo of the retreat host"></div>
  <p class="host-name">Marit Hovland</p>
  <p class="website">www.marithovland.com</p>
</main>
</body>
</html>
```